Vantorique Business Card and Letter Head

We are a leadership assessment consultancy based in Sydney, Australia. We help executive-level decison-makers select leaders for more senior level roles in corporate and government organisations. Our methodology is based on the latest research from the field of neuroscience.
We need a business card design and matching letter head that presents our company, Vantorique, as a:
1. trusted adviser to senior executive-level decison makers
2. niche consultancy who are experts in the field of assessing leadership talent
3. results-focused solution provider who balance scientific methods with pragmatic solutions
The following company details should be used in all designs:
Company Name: Vantorique
Details (for business card):
Daniel Prewett
High Potential Officer
Level 17, Marrowby Tower
14 Tallowin Square
Sydney, NSW 2000 Australia
Phone: 1300 582 714
Mobile: 0412 637 208
Email: daniel.prewett@vantorique.com.au
Website: vantorique.com.au
I have attached the logo for Vantorique (for both a white and black background) - your business card and letter head designs must incoporate this logo and colour scheme.
Thanks for your interest in this project, I'm looking forward to receiving your ideas.
Regards,
Daniel
Target Market(s)
Executive-level decison-makers in corporate and government organisations (e.g., CEO, VP, Head of Human Resources)
Industry/Entity Type
Leadership
Look and feel
Each slider illustrates characteristics of the customer's brand and the style your logo design should communicate.

```html
<!DOCTYPE html>
<html lang="en">
<head>
<meta charset="utf-8">
<title>Vantorique Business Card</title>
<link href="https://fonts.googleapis.com/css2?family=Source+Sans+3:wght@400;600;700&display=swap" rel="stylesheet">
<style>
  :root {
    --brand-red: #bd2e1f;
    --card-white: #ffffff;
    --ink-dark: #3a3a3a;
    --ink-deep: #3d1a13;
    --page-bg: #eeebe8;
    --text-light: #ffffff;
  }
  * { margin: 0; padding: 0; box-sizing: border-box; }
  html, body {
    width: 1200px; height: 1094px; overflow: hidden;
    background: var(--page-bg);
    font-family: "Source Sans 3", sans-serif;
  }
  .canvas { position: relative; width: 1200px; height: 1094px; }
  .card {
    position: absolute; left: 220px; width: 760px; height: 440px;
    border-radius: 40px; overflow: hidden;
    box-shadow: 0 6px 18px rgba(0,0,0,0.18);
  }
  .card-front { top: 80px; display: flex; background: var(--card-white); }
  .card-back { top: 574px; background: var(--brand-red); }

  .front-brand {
    width: 46%; display: flex; align-items: center; justify-content: center; gap: 14px;
  }
  .brand-square { width: 34px; height: 34px; background: var(--brand-red); flex: none; }
  .brand-name-small { font-size: 46px; font-weight: 600; color: var(--ink-dark); letter-spacing: -0.5px; }

  .front-details {
    width: 54%; background: var(--brand-red); color: var(--text-light);
    padding: 44px 40px 0 48px;
  }
  .person-name { font-size: 30px; font-weight: 700; line-height: 1.1; }
  .person-title { font-size: 19px; margin-top: 4px; }
  .address { font-size: 19px; line-height: 1.35; margin-top: 30px; font-style: normal; }
  .contact-list { list-style: none; margin-top: 30px; font-size: 19px; line-height: 1.4; }
  .contact-list li { display: flex; align-items: center; gap: 12px; }
  .contact-list svg { width: 18px; height: 18px; flex: none; }

  .back-brand {
    position: absolute; left: 0; right: 0; top: 130px;
    display: flex; align-items: center; justify-content: center; gap: 26px;
  }
  .brand-square-large { width: 70px; height: 70px; background: var(--ink-deep); flex: none; }
  .brand-name-large { font-size: 100px; font-weight: 600; color: var(--ink-deep); letter-spacing: -1px; line-height: 1; }
  .website {
    position: absolute; left: 0; right: 0; bottom: 66px; text-align: center;
    color: var(--text-light); font-size: 30px; letter-spacing: 3px;
  }
</style>
</head>
<body>
<main class="canvas">
  <section class="card card-front">
    <div class="front-brand">
      <span class="brand-square"></span>
      <span class="brand-name-small">Vantorique</span>
    </div>
    <div class="front-details">
      <p class="person-name">Daniel Prewett</p>
      <p class="person-title">High Potential Officer</p>
      <address class="address">
        Level 17, Marrowby Tower<br>
        14 Tallowin Square<br>
        Sydney, NSW 2000 Australia
      </address>
      <ul class="contact-list">
        <li>
          <svg viewBox="0 0 24 24" aria-hidden="true"><circle cx="12" cy="12" r="11" fill="none" stroke="#fff" stroke-width="2"/><path d="M8 6l3 3-1.5 2a8 8 0 0 0 3.5 3.5L15 13l3 3-2 2C10 17 7 14 6 8z" fill="#fff"/></svg>
          <span>1300 582 714</span>
        </li>
        <li>
          <svg viewBox="0 0 24 24" aria-hidden="true"><rect x="7" y="2" width="10" height="20" rx="2" fill="#fff"/><rect x="9" y="5" width="6" height="9" fill="#bd2e1f"/></svg>
          <span>0412 637 208</span>
        </li>
        <li>
          <svg viewBox="0 0 24 24" aria-hidden="true"><rect x="2" y="5" width="20" height="14" fill="#fff"/><path d="M2 5l10 8 10-8" fill="none" stroke="#bd2e1f" stroke-width="2"/></svg>
          <span>daniel.prewett@vantorique.com.au</span>
        </li>
      </ul>
    </div>
  </section>

  <section class="card card-back">
    <div class="back-brand">
      <span class="brand-square-large"></span>
      <span class="brand-name-large">Vantorique</span>
    </div>
    <p class="website">www.vantorique.com.au</p>
  </section>
</main>
</body>
</html>
```